Geschäftspapiere für Coaching und Talent Management
Professionell und freundlich
Zielgruppe
Zielgruppe: Führungskräfte
Tätigkeit: Führungskräfte Coaching und Talent Management
Aufgabenstellung
- Der Briefbogen soll klar und smart/elegant wirken
- Das Logo wurde gerade neu erstellt und füge ich bei
- Die weiteren Daten lade ich hoch sobald der Gewinner gewählt ist. Bitte beim Design beachten, dass folg Informationen zusätzlich zum Logo auf das Briefpapier sollen:
Postleitzahl und Stadt
Strasse und Hausnummer
Website und Email Kontakt
Umsatz St.Nr

```html
<!DOCTYPE html>
<html lang="de">
<head>
<meta charset="utf-8">
<title>Briefbogen – Kathrin Vollmer</title>
<link rel="stylesheet" href="https://fonts.googleapis.com/css2?family=Lato:wght@400;700&family=Arimo:wght@400&display=swap">
<style>
  :root {
    --ink: #111111;
    --slate: #2c4550;
    --accent: #d4502c;
    --backdrop: #9c9c9c;
    --paper: #ffffff;
    --watermark: #f3f3f3;
  }
  * { margin: 0; padding: 0; box-sizing: border-box; }
  html, body { width: 1200px; height: 1200px; overflow: hidden; background: var(--backdrop); }
  .stage { position: relative; width: 1200px; height: 1200px; }
  .sheet {
    position: absolute; left: 176px; top: 0;
    width: 1240px; height: 1754px;
    background: var(--paper);
    transform: scale(0.684); transform-origin: top left;
    overflow: hidden;
    font-family: "Arimo", Arial, sans-serif;
    color: var(--ink);
  }
  .bar { position: absolute; left: 30px; width: 1181px; height: 14px; }
  .bar--top { top: 17px; background: var(--slate); }
  .bar--bottom { top: 1725px; background: var(--accent); }
  .watermark { position: absolute; left: 140px; top: 1190px; }
  .brand {
    position: absolute; left: 0; right: 0; top: 88px; height: 80px;
    display: flex; align-items: center; justify-content: center;
    font-family: "Lato", sans-serif;
  }
  .brand__dot { width: 40px; height: 40px; border-radius: 50%; background: var(--slate); margin-right: 18px; }
  .brand__name { font-size: 34px; font-weight: 400; color: var(--slate); line-height: 1; }
  .sender { position: absolute; left: 147px; top: 308px; font-family: "Lato", sans-serif; font-size: 14px; color: var(--slate); }
  .sender .sep { color: var(--accent); }
  .recipient { position: absolute; left: 147px; top: 340px; font-size: 22px; line-height: 26.5px; font-style: normal; }
  .contact { position: absolute; left: 932px; top: 305px; height: 96px; border-left: 1.5px solid var(--slate); padding-left: 12px; font-family: "Lato", sans-serif; font-size: 16px; color: var(--slate); }
  .contact__row { display: flex; align-items: center; height: 24px; }
  .contact__row svg { margin-right: 12px; }
  .contact__tax { margin-top: 23px; }
  .fold { position: absolute; left: 0; width: 59px; height: 1px; background: var(--accent); }
  .letter { position: absolute; left: 147px; top: 655px; width: 990px; font-size: 22.5px; line-height: 26.3px; }
  .letter p { margin-bottom: 26.3px; }
  .closing { position: absolute; left: 147px; top: 1288px; font-size: 22.5px; }
</style>
</head>
<body>
<div class="stage">
  <div class="sheet">
    <div class="bar bar--top"></div>

    <svg class="watermark" width="960" height="520" viewBox="0 0 960 520" aria-hidden="true">
      <circle cx="720" cy="260" r="210" fill="none" stroke="var(--watermark)" stroke-width="58"/>
    </svg>

    <header class="brand">
      <div class="brand__dot"></div>
      <div class="brand__name">KATHRIN VOLLMER</div>
    </header>

    <div class="sender">KATHRIN VOLLMER <span class="sep">|</span> Lindenhof 7 <span class="sep">|</span> 60316 Frankfurt am Main</div>

    <address class="recipient">
      Herrn<br>Max Mustermann<br>Musterstraße 00<br><br>01234 Musterstadt
    </address>

    <div class="contact">
      <div class="contact__row">
        <svg width="16" height="12" viewBox="0 0 16 12"><rect x="0.7" y="0.7" width="14.6" height="10.6" fill="none" stroke="var(--accent)" stroke-width="1.4"/><path d="M1 1 L8 7 L15 1" fill="none" stroke="var(--accent)" stroke-width="1.4"/></svg>
        kv@kathrinvollmer-coaching.de
      </div>
      <div class="contact__row">
        <svg width="16" height="16" viewBox="0 0 16 16"><circle cx="8" cy="8" r="7" fill="none" stroke="var(--accent)" stroke-width="1.3"/><ellipse cx="8" cy="8" rx="3" ry="7" fill="none" stroke="var(--accent)" stroke-width="1.1"/><path d="M1 8 H15 M2 4.5 H14 M2 11.5 H14" stroke="var(--accent)" stroke-width="1.1"/></svg>
        www.kathrinvollmer-coaching.de
      </div>
      <div class="contact__tax">Ust-IdNr.: DE418263507</div>
    </div>

    <div class="fold" style="top:620px"></div>
    <div class="fold" style="top:876px"></div>
    <div class="fold" style="top:1240px"></div>

    <main class="letter">
      <p>Dies ist eine Betreffzeile</p>
      <p>Sehr geehrter Herr Mustermann, jeder Setzer hat für diesen Zweck immer etwas Blindtext<br>parat. Blindtext ist im Umfang von einigen tausend Anschlägen, der für die »äußerliche«<br>Gestaltung einer Publikation verwendet und dessen Inhalt unwichtig ist. Man setzt ihn oft zum<br>Beispiel in verschiedenen Schriften und Schriftgrößen, um anderen zu zeigen, wie eine<br>bestimmte Schrift wirkt.</p>
      <p>Oder man montiert auch komplette ganze Seiten mit sinnlosen Streifen von Blindtext, um das<br>spätere Aussehen der Seiten zu simulieren. Blindtext wird allerdings oft nur für die Teile einer<br>Seite verwendet, die in so kleiner Schrift gesetzt werden, dass sie beim »Überfliegen«<br>ungelesen bleiben.</p>
      <p>Jeder Setzer hat für diesen Zweck immer etwas Blindtext parat. Blindtext ist Umfang von<br>einigen tausend Anschlägen, der für die »äußerliche« Gestaltung einer Publikation verwendet<br>und dessen Inhalt unwichtig ist. Oder man montiert auch komplette ganze Seiten mit sinnlosen<br>Streifen von Blindtext, um das spätere Aussehen der Seiten zu simulieren. Blindtext wird<br>allerdings oft nur für die Teile einer Seite verwendet, die in so kleiner Schrift gesetzt werden,<br>dass sie beim »Überfliegen« ungelesen bleiben.</p>
    </main>

    <div class="closing">Mit freundlichen Grüßen</div>

    <div class="bar bar--bottom"></div>
  </div>
</div>
</body>
</html>
```